Brightwell Care Advisors, LLC Business Card update!

would like a classier business card. Our cards currently just have our logo and contact information. Need better use of color and creativity
Logo attached.

Target Market(s)

Potential clients, contacts, existing clients. We are a consulting company

Industry/Entity Type

Business

Contact Information for Business Card

We like our colors but just have a boring card with our logo and a white background. I want something that stands out.

Colors
ec1f27
757575

Requirements
Must have
• Color to stay consistent. Logo provided
Nice to have
• Just better use of color/ design

```html
<!DOCTYPE html>
<html lang="en">
<head>
<meta charset="utf-8">
<title>Brightwell Care Advisors – Business Card</title>
<link href="https://fonts.googleapis.com/css2?family=Source+Sans+3:ital,wght@0,400;0,600;0,700;1,700&display=swap" rel="stylesheet">
<style>
  :root {
    --brand-red: #ec1f27;
    --brand-red-deep: #a8141a;
    --brand-gray: #757575;
    --band-dark: #3b3b3d;
    --text-dark: #4a4a4a;
    --card-bg: #f4f3f0;
    --page-bg: #d8d3cb;
  }
  * { box-sizing: border-box; margin: 0; padding: 0; }
  html, body {
    width: 1200px;
    height: 969px;
    overflow: hidden;
    background: var(--page-bg);
    font-family: "Source Sans 3", sans-serif;
  }
  .business-card {
    position: absolute;
    left: 120px;
    top: 212px;
    width: 960px;
    height: 545px;
    background: var(--card-bg);
    overflow: hidden;
    box-shadow: 0 10px 30px rgba(0,0,0,0.18);
  }
  .brand {
    position: absolute;
    left: 52px;
    top: 52px;
    display: flex;
    align-items: center;
    gap: 14px;
  }
  .brand-mark {
    width: 34px;
    height: 34px;
    background: var(--brand-red);
  }
  .brand-name {
    font-size: 36px;
    font-weight: 600;
    color: var(--brand-red);
    line-height: 1;
  }
  .person-name {
    position: absolute;
    left: 52px;
    top: 196px;
    font-size: 32px;
    font-weight: 700;
    color: var(--brand-red);
  }
  .person-title {
    position: absolute;
    left: 56px;
    top: 238px;
    font-size: 23px;
    color: var(--brand-gray);
  }
  .address {
    position: absolute;
    left: 52px;
    top: 298px;
    font-size: 21px;
    line-height: 33px;
    color: var(--text-dark);
    font-style: normal;
  }
  .contacts {
    position: absolute;
    left: 52px;
    top: 396px;
    display: grid;
    grid-template-columns: 218px auto;
    row-gap: 8px;
    font-size: 21px;
    color: var(--text-dark);
  }
  .contact-item {
    display: flex;
    align-items: center;
    gap: 10px;
    line-height: 30px;
  }
  .contact-icon { width: 20px; height: 20px; fill: var(--brand-red); flex: none; }
  .website {
    position: absolute;
    left: 56px;
    top: 478px;
    font-size: 19px;
    font-weight: 700;
    font-style: italic;
    letter-spacing: 6px;
    color: var(--brand-red-deep);
  }
  .accent-band {
    position: absolute;
    left: 808px;
    top: 0;
    width: 152px;
    height: 402px;
    background: var(--band-dark);
  }
  .accent-block {
    position: absolute;
    left: 808px;
    top: 402px;
    width: 152px;
    height: 143px;
    background: linear-gradient(135deg, var(--brand-red) 0%, var(--brand-red-deep) 100%);
  }
</style>
</head>
<body>
  <section class="business-card">
    <div class="accent-band"></div>
    <div class="accent-block"></div>

    <div class="brand">
      <span class="brand-mark"></span>
      <span class="brand-name">Brightwell Care Advisors</span>
    </div>

    <h1 class="person-name">Dana Whitfield</h1>
    <p class="person-title">Director</p>

    <address class="address">
      Suite 210 Harlow Avenue<br>
      Ohio, Zip 4412, USA
    </address>

    <div class="contacts">
      <div class="contact-item">
        <svg class="contact-icon" viewBox="0 0 20 20"><path d="M2 7c0-3 3-4 8-4s8 1 8 4v2h-4V7H6v2H2z"/><path d="M4 10h12l1 7H3z"/></svg>
        <span>412 555 0183</span>
      </div>
      <div class="contact-item">
        <svg class="contact-icon" viewBox="0 0 20 20"><rect x="5" y="2" width="10" height="5"/><rect x="2" y="7" width="16" height="7" rx="1"/><rect x="5" y="12" width="10" height="6" fill="#fff"/><rect x="6" y="13" width="8" height="4"/></svg>
        <span>412 555 0190</span>
      </div>
      <div class="contact-item">
        <svg class="contact-icon" viewBox="0 0 20 20"><rect x="5" y="1" width="10" height="18" rx="2"/><rect x="7" y="4" width="6" height="10" fill="#fff"/></svg>
        <span>412 555 0190</span>
      </div>
      <div class="contact-item">
        <svg class="contact-icon" viewBox="0 0 20 20"><rect x="2" y="5" width="16" height="11"/><path d="M2 5l8 6 8-6" fill="none" stroke="#fff" stroke-width="1.5"/></svg>
        <span>hello@brightwell.com</span>
      </div>
    </div>

    <p class="website">www.brightwell.com</p>
  </section>
</body>
</html>
```